Postcard flyers for text vouchers

Postcard flyer to drive people to text for local vouchers delivered straight to their mobile, alternatively they can check out the websites.
Double sided, full colour A6 size. 105mm x 148.5mm http://www.brindleprint.example/artwork-guide.html
Postcard will be available in high footfall areas must be eye catching and compelling, but keep message simple. Wording as attached, side one headline grabbing, side two in style of a tag cloud giving a flavour of vouchers/savings available in their local area.
Updates

Project Deadline Extended
Reason: Research has shown wider area for website required therefore by county [Hollowmere Vouchers] rather than smaller regions. Focus on entertainment and shopping for flyer.

Target Market(s)

Target 18-55 year olds
Core 25-45???
male and female

Requirements
Must have
• Stand out

```html
<!DOCTYPE html>
<html lang="en">
<head>
<meta charset="utf-8">
<title>How Much Can You Save? – Text Vouchers Postcard</title>
<link rel="stylesheet" href="https://fonts.googleapis.com/css2?family=Open+Sans:wght@700&family=Nunito:wght@800;900&family=Arimo:wght@400;700&display=swap">
<style>
  :root {
    --paper: #ffffff;
    --sun: #fdc300;
    --sun-light: #ffe100;
    --amber: #f7a400;
    --orange: #f08a00;
    --ink: #111111;
    --charcoal: #2f2b2c;
    --tag-red: #e73c3e;
    --accent-red: #e5232b;
    --body-text: #2a2a2a;
    --tag-text: #f1f1f6;
  }
  * { margin: 0; padding: 0; box-sizing: border-box; }
  html, body { width: 850px; height: 1200px; overflow: hidden; background: var(--paper); }
  .canvas { position: relative; width: 850px; height: 1200px; }

  .postcard {
    position: absolute; left: 33px; top: 33px; width: 784px; height: 1133px;
    border-radius: 28px; overflow: hidden; background: var(--sun);
  }
  .top-strip { position: absolute; left: 0; top: 0; width: 100%; height: 47px; background: var(--charcoal); }
  .header-band {
    position: absolute; left: 0; top: 47px; width: 100%; height: 227px;
    background: linear-gradient(180deg, var(--sun-light) 0%, var(--sun) 55%, var(--amber) 100%);
  }
  .swirl-field {
    position: absolute; left: 0; top: 274px; width: 100%; height: 340px;
    background: linear-gradient(180deg, var(--charcoal) 0%, var(--charcoal) 35%, var(--orange) 75%, var(--sun) 100%);
    border-bottom-right-radius: 60% 40%;
    border-bottom-left-radius: 30% 20%;
  }

  .headline { position: absolute; font-family: "Open Sans", sans-serif; font-weight: 700; color: var(--ink); line-height: 1; white-space: nowrap; }
  .headline-how { left: 74px; top: 49px; font-size: 88px; }
  .headline-can { left: 432px; top: 132px; font-size: 46px; letter-spacing: -1px; }
  .headline-save { left: 357px; top: 139px; font-size: 125px; letter-spacing: -2px; }

  .tagline {
    position: absolute; left: 50px; top: 300px;
    font-family: "Nunito", sans-serif; font-weight: 900; font-size: 43px; line-height: 42px;
    color: var(--paper); white-space: nowrap;
    text-shadow: -2px -2px 0 var(--charcoal), 2px -2px 0 var(--charcoal), -2px 2px 0 var(--charcoal), 2px 2px 0 var(--charcoal), 0 3px 0 var(--charcoal);
  }

  .voucher-tag {
    position: absolute; left: 333px; top: 380px; width: 401px; height: 118px;
    background: var(--tag-red); transform: rotate(-4deg);
    outline: 2px dotted #ffb0b3; outline-offset: -7px;
    box-shadow: 3px 5px 6px rgba(0,0,0,0.3);
    display: flex; align-items: center; justify-content: center;
    font-family: "Nunito", sans-serif; font-weight: 800; font-size: 94px; color: var(--tag-text);
  }

  .instructions { position: absolute; left: 74px; top: 607px; font-family: "Arimo", sans-serif; color: var(--body-text); white-space: nowrap; }
  .instructions-lead { font-size: 26.5px; line-height: 30px; margin-bottom: 23px; }
  .area-line { font-size: 24px; font-weight: 700; line-height: 37px; }
  .text-code { color: var(--accent-red); font-size: 30px; }

  .redeem { position: absolute; left: 178px; top: 806px; font-family: "Arimo", sans-serif; font-size: 26.7px; line-height: 42px; color: var(--body-text); white-space: nowrap; }
  .redeem-easy { color: var(--accent-red); font-weight: 700; font-size: 52px; letter-spacing: -1px; margin-left: 8px; line-height: 0; }

  .small-print { position: absolute; left: 74px; top: 922px; font-family: "Arimo", sans-serif; font-weight: 700; font-size: 18.6px; line-height: 25px; color: var(--body-text); white-space: nowrap; }

  .websites { position: absolute; left: 0; top: 1016px; width: 784px; text-align: center; font-family: "Arimo", sans-serif; font-size: 21px; line-height: 27px; color: var(--body-text); list-style: none; }
</style>
</head>
<body>
<div class="canvas">
  <div class="postcard">
    <div class="top-strip"></div>
    <div class="header-band" role="img" aria-label="Yellow band with decorative swirl pattern"></div>
    <div class="swirl-field" role="img" aria-label="Dark and orange decorative swirl ornament"></div>

    <div class="headline headline-how">How Much</div>
    <div class="headline headline-can">Can You</div>
    <div class="headline headline-save">Save?</div>

    <p class="tagline">Your local money saving<br>are waiting for you</p>
    <div class="voucher-tag">Vouchers</div>

    <div class="instructions">
      <p class="instructions-lead">Simply choose your area and text as follows:</p>
      <p class="area-line">For savings in Malvern text <span class="text-code">voucher m to 64321</span></p>
      <p class="area-line">For savings in Worcester text <span class="text-code">voucher w to 64321</span></p>
      <p class="area-line">For savings in Hereford text <span class="text-code">voucher h to 64321</span></p>
    </div>

    <div class="redeem">
      <p>To redeem simply quote the voucher</p>
      <p>code or print off.<span class="redeem-easy">Easy</span></p>
    </div>

    <p class="small-print">Standard text rates apply. No spam policy. Unsubscibe at any time.<br>See your voucher websites for even more savings</p>

    <ul class="websites">
      <li>www.malvernsavers.example</li>
      <li>www.worcestersavers.example</li>
      <li>www.herefordsavers.example</li>
    </ul>
  </div>
</div>
</body>
</html>
```